Fence Contractor Website Design

We are working with Yardline Works. They are a local fencing and automatic gate installer and in need of a new website design.
Some sites to use for inspiration:
https://pinevalebarrier.example
https://marwickrails.example
https://www.tellurpostsandboards.example
https://www.grovanpaneling.example
Thank you for taking the time to consider designing a website for us. We are web developers based in Stockton, CA, USA. Most of our projects go through the same process. Understanding this process may help you win a project with us. We custom-code all of our websites in-house. We don’t have any requirements as to what tools you use for your design, but we prefer Figma files. For any design that we label as four-stars, we send it to the client for review. The client picks the final design they want us to use. Once we complete this process, we will continue to show additional clients all the four-star sites and purchase them later. Your designs will have multiple chances to sell. For better chances of success, we ask that you follow these guidelines.
IMAGES:
If you use any images or icons in the design, we ask that you have a link to the asset so we can purchase the image/icon. Most of the designs we submit do not have the customer’s images on them unless they have some great images. Be creative; show us the feeling you are trying to portray with your image choices. Use any royalty-free site you choose. We subscribe to Stockvane and mainly use their images, but we can purchase images outside of Stockvane.
PLEASE NOTE: we will not submit designs to clients with watermarks on the images.
FONTS:
We ask that you identify the fonts used in the design. This can be done in a message if you want. We typically use Google Fonts and Stockvane Fonts.
CONTENT:
We're always open to different content and ideas. We often submit designs with stock images so the client can see our vision. We typically take pictures after the website launch to use their images with our vision. Lorem Ipsum is fine for paragraphs, but we ask that you write the headers in correct English. We want to be able to show the vision and identify the sections of the website.
INSPIRATION:
We typically add a couple of links in the brief of websites we like to help you get started in your design.
REVISIONS:
We do not often ask for revisions of the designs unless we see something in the design that may not appeal to the client. If there are slight changes that we want to make, we do that in the development process.
FEEDBACK:
We rarely give feedback on designs during the design process. We are working on many website projects and do not have the time to provide feedback. We usually respond if your request is well thought out and asks specific questions, but a note asking “feedback, please” usually goes unanswered.
Number of Pages Required
1 page
Look and feel
Each slider illustrates characteristics of the customer's brand and the style your logo design should communicate.

```html
<!DOCTYPE html>
<html lang="en">
<head>
<meta charset="utf-8">
<title>Yardline Works – Fencing &amp; Gates</title>
<link href="https://fonts.googleapis.com/css2?family=Titillium+Web:wght@300;400;600;700&display=swap" rel="stylesheet">
<style>
:root{
  --navy:#1d2a4a;
  --navy-deep:#16213d;
  --red:#f20d0d;
  --red-dark:#c20a1e;
  --ink:#222b3d;
  --muted:#4a5264;
  --pink-bg:#fdf0ee;
  --blue-bg:#eef3fa;
  --white:#ffffff;
  --line:#e4e7ee;
}
*{box-sizing:border-box;margin:0;padding:0}
html,body{width:1200px;height:3995px;overflow:hidden}
body{font-family:"Titillium Web",sans-serif;color:var(--ink);background:var(--white);position:relative}
a{color:inherit;text-decoration:none}

/* top bar */
.topbar{position:absolute;top:0;left:0;width:1200px;height:34px;background:var(--navy)}
.topbar .red-side{position:absolute;right:0;top:0;height:34px;width:510px;background:var(--red);clip-path:polygon(16px 0,100% 0,100% 100%,0 100%)}
.topbar .email{position:absolute;left:99px;top:6px;color:#fff;font-size:16px;display:flex;gap:10px;align-items:center}
.topbar .phone{position:absolute;right:99px;top:6px;color:#fff;font-size:16px;font-weight:600;display:flex;gap:8px;align-items:center}
.nav{position:absolute;top:34px;left:0;width:1200px;height:66px;background:#fff}
.nav ul{list-style:none;position:absolute;top:24px;display:flex;gap:40px;font-size:14px;text-transform:uppercase}
.nav .left{left:99px}
.nav .right{left:710px}
.nav li.active{border-bottom:2px solid var(--red);padding-bottom:4px}
.brand{position:absolute;left:532px;top:0;width:136px;height:100px;background:#fff;border-radius:0 0 16px 16px;display:flex;flex-direction:column;align-items:center;justify-content:center;gap:6px;z-index:5}
.brand .dot{width:24px;height:24px;border-radius:50%;background:var(--red)}
.brand .name{font-weight:700;font-size:15px;color:var(--navy);line-height:1}
.btn{display:inline-flex;align-items:center;gap:10px;background:var(--navy);color:#fff;border-radius:20px;font-size:13px;text-transform:uppercase;padding:0 6px 0 14px;height:36px}
.btn .star{width:22px;height:22px;border-radius:50%;background:var(--red);display:flex;align-items:center;justify-content:center}
.nav .quote{position:absolute;left:963px;top:16px;height:38px}

/* hero */
.hero{position:absolute;top:100px;left:0;width:1200px;height:528px;background:linear-gradient(180deg,#8fa4b8 0%,#b9c6b4 40%,#6f8f4c 62%,#e9ece8 80%,#f4f5f2 100%)}
.hero h1{position:absolute;left:99px;top:112px;font-size:50px;line-height:54px;font-weight:700;color:var(--navy);text-transform:uppercase}
.hero h1 .red{color:var(--red);font-weight:400;display:block}
.hero h1 .thin{font-weight:400;display:block}
.hero .btn{position:absolute;left:104px;top:300px;height:38px}
.hero svg.curve{position:absolute;left:0;bottom:0}

/* section titles */
.title{position:absolute;left:0;width:1200px;text-align:center;font-size:44px;font-weight:700;color:var(--navy);text-transform:uppercase;display:flex;justify-content:center;align-items:center;gap:10px}
.title .red{color:var(--red);font-weight:400}
.title .dash{display:inline-block;width:40px;height:2px;background:var(--navy)}

/* services */
.arrows{position:absolute;top:756px;left:1039px;display:flex;gap:6px}
.arrow{width:28px;height:28px;border-radius:50%;display:flex;align-items:center;justify-content:center;border:1.5px solid var(--navy);background:#fff}
.arrow.fill{background:var(--red);border-color:var(--red)}
.card{position:absolute;top:795px;width:242px;height:375px;background:#fff;border:1px solid var(--line);border-radius:10px;box-shadow:0 2px 8px rgba(0,0,0,.08);text-align:center}
.card .ph{position:absolute;left:15px;top:18px;width:212px;height:140px;border-radius:8px}
.card h3{position:absolute;top:178px;left:0;width:100%;font-size:18px;font-weight:400;text-transform:uppercase;color:var(--ink)}
.card p{position:absolute;left:16px;right:16px;top:210px;font-size:12.5px;line-height:16px;text-align:left;color:var(--muted)}
.card .more{position:absolute;left:71px;top:330px;width:100px;height:28px;border-radius:14px;background:var(--navy);color:#fff;font-size:12px;line-height:28px}

/* about */
.about{position:absolute;top:1229px;left:0;width:1200px;height:487px;background:var(--pink-bg)}
.about .ph1{position:absolute;left:99px;top:76px;width:296px;height:312px;border-radius:24px;background:linear-gradient(180deg,#7fa2c4,#a9b9c9 55%,#d7dbd6)}
.about .ph2{position:absolute;left:294px;top:222px;width:200px;height:206px;border-radius:24px;border:4px solid #fff;background:linear-gradient(180deg,#5b8fd6,#c9d7e6 50%,#f1f1ee)}
.about h2{position:absolute;left:532px;top:70px;font-size:44px;font-weight:700;color:var(--navy);text-transform:uppercase;display:flex;gap:10px;align-items:center}
.about h2 .red{color:var(--red);font-weight:400}
.about h2 .dash{width:40px;height:2px;background:var(--navy)}
.about p{position:absolute;left:532px;top:138px;width:570px;font-size:13.5px;line-height:31px}
.about .btn{position:absolute;left:535px;top:378px}

/* why */
.why{position:absolute;top:1716px;left:0;width:1200px;height:550px;background:var(--blue-bg)}
.why .sub{position:absolute;top:168px;left:0;width:1200px;text-align:center;font-size:14px}
.feat{position:absolute;top:307px;width:242px;height:158px;background:#fff;border:1px solid var(--line);border-radius:10px;text-align:center}
.feat .ico{position:absolute;left:77px;top:-44px;width:88px;height:88px;border-radius:50%;background:radial-gradient(circle at 40% 35%,var(--red),var(--red-dark) 70%,#7c0b2b);display:flex;align-items:center;justify-content:center}
.feat h3{position:absolute;top:60px;width:100%;font-size:18px;font-weight:400;text-transform:uppercase}
.feat p{position:absolute;top:92px;left:30px;right:30px;font-size:14px;line-height:20px;color:var(--muted)}

/* gallery */
.gal{position:absolute;top:2444px;width:219px;height:227px}
.gal-arrow{position:absolute;top:2543px;width:26px;height:26px;border-radius:50%;background:var(--red);display:flex;align-items:center;justify-content:center}

/* testimonial */
.testi{position:absolute;top:2736px;left:0;width:1200px;height:423px;background:linear-gradient(90deg,#eceef1,#f7f8f9 60%,#e9ebee)}
.testi .kicker{position:absolute;left:99px;top:85px;font-size:17px;color:var(--red);display:flex;gap:8px;align-items:center}
.testi .kicker span{width:40px;height:1.5px;background:var(--muted)}
.testi .quote-mark{position:absolute;left:99px;top:118px;width:62px;height:40px}
.testi h2{position:absolute;left:99px;top:110px;font-size:40px;font-weight:700;color:var(--navy);line-height:48px}
.testi p{position:absolute;left:99px;top:186px;width:460px;font-size:12.5px;line-height:26px;color:var(--muted)}
.testi .who{position:absolute;left:104px;top:304px;font-size:13px}
.testi .circle{position:absolute;left:716px;top:46px;width:326px;height:326px;border-radius:50%;background:radial-gradient(circle,#3b5a95,#b9c3d4 70%,#e3e6eb)}

/* footer */
.footer{position:absolute;top:3612px;left:0;width:1200px;height:383px;background:var(--navy-deep)}
.contact{position:absolute;top:3216px;left:197px;width:806px;height:424px;background:var(--red);border-radius:14px}
.contact h2{position:absolute;top:42px;width:100%;text-align:center;font-size:42px;color:#fff;font-weight:700}
.contact h2 span{font-weight:400}
.info{position:absolute;left:70px;display:flex;align-items:center;gap:10px;color:#fff;font-size:15px;line-height:20px}
.info .c{width:56px;height:56px;border-radius:50%;background:#fff;display:flex;align-items:center;justify-content:center;flex:none}
.field{position:absolute;background:#fff;border-radius:14px;height:34px;font-size:12px;color:#9aa0ab;padding:9px 16px}
.send{position:absolute;left:483px;top:342px;width:104px;height:34px;border:2px solid #fff;border-radius:17px;background:var(--navy);color:#fff;font-size:13px;text-align:center;line-height:30px}
.f-brand{position:absolute;left:540px;top:3680px;width:120px;height:120px;border-radius:50%;background:#fff;display:flex;flex-direction:column;align-items:center;justify-content:center;gap:6px}
.f-brand .dot{width:20px;height:20px;border-radius:50%;background:var(--red)}
.f-brand .name{font-weight:700;font-size:15px;color:var(--navy)}
.f-call{position:absolute;top:3811px;width:1200px;text-align:center;color:var(--red);font-size:15px}
.f-call b{font-weight:600}
.f-links{position:absolute;top:3846px;width:1200px;display:flex;justify-content:center;gap:40px;color:#fff;font-size:14px;text-transform:uppercase;list-style:none}
.socials{position:absolute;top:3893px;left:534px;display:flex;gap:8px}
.socials span{width:38px;height:38px;border-radius:50%;border:2px solid #fff;background:var(--red)}
.socials span:first-child{background:transparent}
.copy{position:absolute;top:3955px;width:1200px;text-align:center;color:#fff;font-size:12px}
</style>
</head>
<body>

<header>
  <div class="topbar">
    <div class="red-side"></div>
    <div class="email">
      <svg width="20" height="20" viewBox="0 0 20 20"><circle cx="10" cy="10" r="10" fill="#fff"/><rect x="5" y="6.5" width="10" height="7" rx="1" fill="none" stroke="#1d2a4a" stroke-width="1.3"/><path d="M5 7l5 3.5L15 7" fill="none" stroke="#1d2a4a" stroke-width="1.3"/></svg>
      hello@yardlineworks.example
    </div>
    <div class="phone">
      <svg width="18" height="18" viewBox="0 0 20 20"><circle cx="10" cy="10" r="10" fill="#fff"/><path d="M7 5.5l1.6 2.2-1 1.2c.6 1.3 1.6 2.3 2.9 2.9l1.2-1 2.2 1.6-.7 1.8c-3.8 0-7.3-3.5-7.3-7.3z" fill="#f20d0d"/></svg>
      +44 210-555-0148
    </div>
  </div>
  <nav class="nav">
    <ul class="left">
      <li class="active">Home</li><li>About</li><li>Services</li><li>Gallery</li>
    </ul>
    <ul class="right">
      <li>Why Choose Us</li><li>Contact Us</li>
    </ul>
    <a class="btn quote">Get a Quote <span class="star"><svg width="12" height="12" viewBox="0 0 12 12"><path d="M6 0l1.8 3.8 4.2.5-3.1 2.9.8 4.1L6 9.3 2.3 11.3l.8-4.1L0 4.3l4.2-.5z" fill="#fff"/></svg></span></a>
  </nav>
  <div class="brand"><span class="dot"></span><span class="name">Yardline Works</span></div>
</header>

<section class="hero" role="img" aria-label="Photo of a white picket fence in front of a blue house and garden">
  <h1>We're strong enough<span class="red">to handle any challenge</span><span class="thin">just like our fences</span></h1>
  <a class="btn">Free Estimates <span class="star"><svg width="12" height="12" viewBox="0 0 12 12"><path d="M6 0l1.8 3.8 4.2.5-3.1 2.9.8 4.1L6 9.3 2.3 11.3l.8-4.1L0 4.3l4.2-.5z" fill="#fff"/></svg></span></a>
  <svg class="curve" width="1200" height="60" viewBox="0 0 1200 60"><path d="M0 60 Q600 -30 1200 60Z" fill="#fff"/><path d="M420 16 Q600 -6 780 16" fill="none" stroke="#f20d0d" stroke-width="3"/></svg>
</section>

<section class="services">
  <h2 class="title" style="top:676px"><span class="dash"></span>Our <span class="red">Services</span><span class="dash"></span></h2>
  <div class="arrows">
    <span class="arrow"><svg width="10" height="10" viewBox="0 0 10 10"><path d="M7 1L3 5l4 4" fill="none" stroke="#1d2a4a" stroke-width="1.6"/></svg></span>
    <span class="arrow fill"><svg width="10" height="10" viewBox="0 0 10 10"><path d="M3 1l4 4-4 4" fill="none" stroke="#fff" stroke-width="1.6"/></svg></span>
  </div>
  <article class="card" style="left:99px">
    <div class="ph" role="img" aria-label="Photo of a worker staining a wooden fence" style="background:linear-gradient(135deg,#8a4a2c,#c0714a 50%,#6b3a22)"></div>
    <h3>Fence Installation</h3>
    <p>Our experienced professionals help you select and install the type of high-quality fencing and perimeter control solutions that best meets your project specifications and needs of your property.</p>
    <a class="more">Read More</a>
  </article>
  <article class="card" style="left:355px">
    <div class="ph" role="img" aria-label="Photo of a modern automatic metal and wood gate" style="background:linear-gradient(135deg,#2a2a2a,#a5562e 50%,#444)"></div>
    <h3>Automatic Gates</h3>
    <p>Our experienced professionals help you select and install the type of high-quality fencing and perimeter control solutions that best meets your project specifications and needs of your property.</p>
    <a class="more">Read More</a>
  </article>
  <article class="card" style="left:609px">
    <div class="ph" role="img" aria-label="Photo of a green custom metal fence along a concrete path" style="background:linear-gradient(180deg,#5fcf3a,#8bd46c 40%,#a7a9a6)"></div>
    <h3>Custom Fabrication</h3>
    <p>Our experienced professionals help you select and install the type of high-quality fencing and perimeter control solutions that best meets your project specifications and needs of your property.</p>
    <a class="more">Read More</a>
  </article>
  <article class="card" style="left:861px">
    <div class="ph" role="img" aria-label="Photo of a team of consultants reviewing plans" style="background:linear-gradient(135deg,#e9eef2,#8aa0b6 50%,#3b4a5e)"></div>
    <h3>Project Consulting</h3>
    <p>Our experienced professionals help you select and install the type of high-quality fencing and perimeter control solutions that best meets your project specifications and needs of your property.</p>
    <a class="more">Read More</a>
  </article>
</section>

<section class="about">
  <div class="ph1" role="img" aria-label="Photo of a blue house with a white picket fence"></div>
  <div class="ph2" role="img" aria-label="Close photo of white picket fence boards against the sky"></div>
  <h2>About <span class="red">Us</span><span class="dash"></span></h2>
  <p>Lorem Ipsum is simply dummy text of the printing and typesetting industry. Lorem Ipsum has been the industry's standard dummy text ever since the 1500s, when an unknown printer took a galley of type and scrambled it to make a type specimen book. It has survived not only five centuries, but also the leap into electronic typesetting, remaining essentially unchanged. It was popularised in the 1960s with the release of Presmark sheets containing Lorem Ipsum passages, and more recently with desktop publishing software like Quillset Layout including versions of Lorem Ipsum.</p>
  <a class="btn">Read More <span class="star"><svg width="12" height="12" viewBox="0 0 12 12"><path d="M6 0l1.8 3.8 4.2.5-3.1 2.9.8 4.1L6 9.3 2.3 11.3l.8-4.1L0 4.3l4.2-.5z" fill="#fff"/></svg></span></a>
</section>

<section class="why">
  <h2 class="title" style="top:78px"><span class="dash"></span>Why <span class="red">Choose Us ?</span><span class="dash"></span></h2>
  <p class="sub">Lorem Ipsum is simply dummy text of the printing and typesetting industry. Lorem Ipsum has</p>
  <div class="feat" style="left:99px">
    <div class="ico"><svg width="40" height="40" viewBox="0 0 40 40"><circle cx="20" cy="20" r="15" fill="none" stroke="#fff" stroke-width="3"/><path d="M12 20l6 6 11-12" fill="none" stroke="#fff" stroke-width="3.5"/></svg></div>
    <h3>Experience</h3><p>We have been in business since 1983.</p>
  </div>
  <div class="feat" style="left:352px">
    <div class="ico"><svg width="40" height="40" viewBox="0 0 40 40"><path d="M20 4c-6.5 0-11 4.7-11 10.5C9 22 20 34 20 34s11-12 11-19.5C31 8.7 26.5 4 20 4z" fill="#fff"/><circle cx="20" cy="14.5" r="4.5" fill="#c20a1e"/><ellipse cx="20" cy="35" rx="10" ry="2.5" fill="none" stroke="#fff" stroke-width="2"/></svg></div>
    <h3>Size &amp; Locations</h3><p>We have been in business since 1983.</p>
  </div>
  <div class="feat" style="left:605px">
    <div class="ico"><svg width="46" height="40" viewBox="0 0 46 40"><g fill="#fff"><path d="M5 10l3-4 3 4v22H5z"/><path d="M14 10l3-4 3 4v22h-6z"/><path d="M23 10l3-4 3 4v22h-6z"/><path d="M32 10l3-4 3 4v22h-6z"/><rect x="2" y="14" width="42" height="3"/><rect x="2" y="24" width="42" height="3"/></g></svg></div>
    <h3>Customers</h3><p>We have been in business since 1983.</p>
  </div>
  <div class="feat" style="left:858px">
    <div class="ico"><svg width="40" height="40" viewBox="0 0 40 40"><circle cx="20" cy="14" r="10" fill="#fff"/><text x="20" y="19" text-anchor="middle" font-family="Titillium Web,sans-serif" font-weight="700" font-size="14" fill="#c20a1e">$</text><path d="M5 28h8l6 3h9l6-4" fill="none" stroke="#fff" stroke-width="3" stroke-linecap="round"/></svg></div>
    <h3>Online Specials</h3><p>We have been in business since 1983.</p>
  </div>
</section>

<section class="gallery">
  <h2 class="title" style="top:2334px"><span class="dash"></span>Our <span class="red">Gellary</span><span class="dash"></span></h2>
  <span class="gal-arrow" style="left:98px"><svg width="10" height="10" viewBox="0 0 10 10"><path d="M7 1L3 5l4 4" fill="none" stroke="#fff" stroke-width="1.8"/></svg></span>
  <div class="gal" style="left:138px;background:linear-gradient(135deg,#2d3a52,#7d8ea8 50%,#1f2a3c)" role="img" aria-label="Photo of a gloved hand on a dark metal fence"></div>
  <div class="gal" style="left:372px;background:linear-gradient(180deg,#6d6d6f,#3b3b3d 50%,#8a8678)" role="img" aria-label="Photo of a dark modern gate between stone walls"></div>
  <div class="gal" style="left:606px;background:linear-gradient(180deg,#3a8fd6,#7fb7e3 60%,#3f6b2e)" role="img" aria-label="Photo of barbed wire fence against a blue sky"></div>
  <div class="gal" style="left:842px;background:linear-gradient(180deg,#a9c0d6,#6b8f4e 55%,#eceeea)" role="img" aria-label="Photo of a white picket fence in front of a blue house"></div>
  <span class="gal-arrow" style="left:1075px"><svg width="10" height="10" viewBox="0 0 10 10"><path d="M3 1l4 4-4 4" fill="none" stroke="#fff" stroke-width="1.8"/></svg></span>
</section>

<section class="testi">
  <div class="kicker">TESTIMONIAL <span></span></div>
  <svg class="quote-mark" viewBox="0 0 62 40"><path d="M4 40V22C4 10 10 4 22 2v8c-6 2-8 6-8 10h8v20zM36 40V22c0-12 6-18 18-20v8c-6 2-8 6-8 10h8v20z" fill="#f20d0d" opacity=".45"/></svg>
  <h2>WHAT THEY SAY</h2>
  <p>Lorem Ipsum is simply dummy text of the printing and typesetting industry. Lorem Ipsum has been the industry's standard dummy text ever since the 1500s, when an unknown printer took a galley of type and scrambled it to make a type specimen book. It has sur</p>
  <div class="who">Dara Quellin</div>
  <div class="circle" role="img" aria-label="Photo of a group of happy customers giving thumbs up"></div>
</section>

<footer class="footer"></footer>

<section class="contact">
  <h2>GET <span>IN TOUCH</span></h2>
  <div class="info" style="top:146px">
    <span class="c"><svg width="26" height="26" viewBox="0 0 26 26"><path d="M13 2c-4.5 0-8 3.3-8 7.6C5 15 13 24 13 24s8-9 8-14.4C21 5.3 17.5 2 13 2z" fill="#f20d0d"/><circle cx="13" cy="10" r="3" fill="#fff"/></svg></span>
    <span>4180 Birchmoor Lane<br>Stockdale</span>
  </div>
  <div class="info" style="top:218px">
    <span class="c"><svg width="26" height="26" viewBox="0 0 26 26"><path d="M7 4l3.5 4.5-2 2.3c1.2 2.7 3.3 4.8 6 6l2.3-2L21.3 18l-1.5 3.8C12 21.8 4.2 14 4.2 6.2z" fill="#f20d0d"/></svg></span>
    <span>Call Us<br><b style="font-weight:600">+44 210-555-0148</b></span>
  </div>
  <div class="info" style="top:290px">
    <span class="c"><svg width="26" height="26" viewBox="0 0 26 26"><rect x="4" y="7" width="18" height="13" rx="2" fill="#f20d0d"/><path d="M4.5 8l8.5 6 8.5-6" fill="none" stroke="#fff" stroke-width="1.6"/></svg></span>
    <span>hello@yardlineworks.example</span>
  </div>
  <div class="field" style="left:366px;top:143px;width:166px">Name</div>
  <div class="field" style="left:540px;top:143px;width:166px">Last Name</div>
  <div class="field" style="left:366px;top:188px;width:166px">E mail</div>
  <div class="field" style="left:540px;top:188px;width:166px">Phone Number</div>
  <div class="field" style="left:366px;top:234px;width:340px;height:88px">Message</div>
  <a class="send">SEND</a>
</section>

<div class="f-brand"><span class="dot"></span><span class="name">Yardline Works</span></div>
<div class="f-call">Call Us <b>+44 210-555-0148</b></div>
<ul class="f-links"><li>Home</li><li>About</li><li>Services</li><li>Gallerywhy</li><li>Choose Us</li><li>Contact Us</li></ul>
<div class="socials" aria-label="Social links"><span></span><span></span><span></span></div>
<div class="copy">2025 copy rights. All Rights Reserved.</div>

</body>
</html>
```